Dental Office Looking for Modern, simple business cards

We just acquired our logo. Now we would like to make business cards. We are a dental office with two doctors. We are husband and wife and have a small boutique dental practice in a small town. We love our patients and they are always asking us to give our business cards to their friends. Please help us make business cards :-)

Target Market(s)

30-60 yr old

Industry/Entity Type

Dental Clinic

Contact Information for Business Card

Birch Hollow Dental P.C.
Family and Cosmetic Dentistry
4827 Dunmore Rd. Schenectady NY 12309
Tel: 518 642 8817 Fax: 518 642 8830

Dr. Tomas K. Elridge DDS
Dr. Marisol Anne Whitby DDS

Font styles to use
Serif
Sans Serif

Requirements
Must have
• Simple clean design, modern, colorful. Should incorporate the logo.
Nice to have
• dental imagery ( teeth, smile, etc ...).

```html
<!DOCTYPE html>
<html lang="en">
<head>
<meta charset="utf-8">
<title>Birch Hollow Dental – Business Cards</title>
<link href="https://fonts.googleapis.com/css2?family=Lato:wght@400;700&display=swap" rel="stylesheet">
<style>
  :root {
    --backdrop: #3a3c40;
    --brand-blue: #1478c2;
    --brand-blue-dark: #0f6cb3;
    --ink-grey: #444a50;
    --rule-grey: #8a8e93;
    --card-white: #ffffff;
  }
  * { box-sizing: border-box; margin: 0; padding: 0; }
  html, body {
    width: 1200px; height: 880px; overflow: hidden;
    background: var(--backdrop);
    font-family: "Lato", Arial, sans-serif;
  }
  .stage { position: relative; width: 1200px; height: 880px; }
  .card {
    position: absolute; width: 620px; height: 354px;
    border-radius: 22px; overflow: hidden;
    box-shadow: 0 18px 40px rgba(0,0,0,.45);
  }
  /* Front */
  .card-front { left: 90px; top: 66px; background: var(--brand-blue); color: #fff; }
  .card-front .wordmark {
    position: absolute; left: 0; right: 0; top: 118px;
    display: flex; align-items: center; justify-content: center; gap: 14px;
  }
  .wordmark-dot { width: 18px; height: 18px; border-radius: 50%; background: currentColor; }
  .wordmark-name { font-weight: 700; font-size: 40px; letter-spacing: 2px; text-transform: uppercase; }
  .card-front .tagline {
    position: absolute; left: 0; right: 0; top: 258px; text-align: center;
    font-weight: 700; font-size: 17px; letter-spacing: 1.5px;
  }
  /* Back */
  .card-back { left: 490px; top: 458px; background: var(--card-white); }
  .card-back .wordmark {
    position: absolute; right: 40px; top: 34px;
    display: flex; align-items: center; gap: 10px; color: var(--brand-blue);
  }
  .card-back .wordmark-name { font-size: 28px; }
  .card-back .wordmark-dot { width: 13px; height: 13px; }
  .divider { position: absolute; height: 1px; background: var(--rule-grey); }
  .divider-top { right: 40px; top: 92px; width: 330px; }
  .divider-mid { left: 36px; top: 228px; width: 250px; }
  .doctors {
    position: absolute; left: 36px; top: 160px;
    color: var(--brand-blue); font-weight: 700; font-size: 23px; line-height: 30px;
  }
  .contacts {
    position: absolute; left: 36px; top: 244px; list-style: none;
    color: var(--ink-grey); font-size: 17px; line-height: 28px;
  }
  .contacts li { display: flex; align-items: center; gap: 12px; }
  .contacts svg { width: 15px; height: 15px; fill: var(--brand-blue); flex: none; }
  .practice {
    position: absolute; right: 40px; top: 112px; text-align: right;
    font-size: 16px; line-height: 23px; color: var(--ink-grey);
  }
  .practice-name { color: var(--brand-blue); }
  .base-band { position: absolute; left: 0; right: 0; bottom: 0; height: 12px; display: flex; }
  .base-band .band-grey { flex: 0 0 62%; background: #9a9da1; }
  .base-band .band-blue { flex: 1; background: var(--brand-blue-dark); }
</style>
</head>
<body>
<main class="stage">
  <section class="card card-front" aria-label="Business card front">
    <div class="wordmark"><span class="wordmark-dot"></span><span class="wordmark-name">Birch Hollow Dental</span></div>
    <p class="tagline">Family and Cosmetic Dentistry</p>
  </section>

  <section class="card card-back" aria-label="Business card back">
    <div class="wordmark"><span class="wordmark-dot"></span><span class="wordmark-name">Birch Hollow Dental</span></div>
    <div class="divider divider-top"></div>
    <div class="practice">
      <p class="practice-name">Birch Hollow Dental P.C.</p>
      <p>4827 Dunmore Rd. Schenectady</p>
      <p>NY 12309</p>
    </div>
    <div class="doctors">
      <p>Dr. Tomas K. Elridge DDS</p>
      <p>Dr. Marisol Anne Whitby DDS</p>
    </div>
    <div class="divider divider-mid"></div>
    <ul class="contacts">
      <li><svg viewBox="0 0 24 24" aria-hidden="true"><path d="M6.6 10.8a15.1 15.1 0 0 0 6.6 6.6l2.2-2.2c.3-.3.7-.4 1-.2 1.1.4 2.3.6 3.6.6.6 0 1 .4 1 1V20c0 .6-.4 1-1 1A17 17 0 0 1 3 4c0-.6.4-1 1-1h3.5c.6 0 1 .4 1 1 0 1.3.2 2.5.6 3.6.1.3 0 .7-.2 1z"/></svg>518 642 8817</li>
      <li><svg viewBox="0 0 24 24" aria-hidden="true"><path d="M7 3h10v5H7zM4 9h16a2 2 0 0 1 2 2v6h-4v4H6v-4H2v-6a2 2 0 0 1 2-2zm4 6v4h8v-4z"/></svg>518 642 8830</li>
      <li><svg viewBox="0 0 24 24" aria-hidden="true"><path d="M2 5h20v14H2zm2 2v.5l8 5 8-5V7l-8 5z"/></svg>hello@birchhollowdental.com</li>
    </ul>
    <div class="base-band"><span class="band-grey"></span><span class="band-blue"></span></div>
  </section>
</main>
</body>
</html>
```